Beer Bottle Label, Quarrystone Brewing, Beaumont Homestead

Title: Quarrystone Label Design – Beaumont Homestead
Date: November 6, 2015
Contacts: Tom Brennick

PROJECT OVERVIEW
Objective:
• Create look & feel for Quarrystone beer bottle

Description:
• Label design template for beer bottle that carries Quarrystone branding and allows for Handwritten ABV, IBU, SRM, Batch# and Bottle#

Other considerations:
• Quarrystone artwork per beer type

CREATIVE EXECUTION
Branding:
• Brand personality: Scientific, Cultural with purpose
• Fonts: Road Movie, Rockwell Nexta Rust, Lavenderia
• Colors: Orange (C:2 M:72 Y:100 K:0) & black (C:0 M:0 Y:0 K:100)
• Logo: Provided (Quarrystonebottlelabel.ai.jpg) (QuarrystoneLogo-Enhanced.psd)

Beer Description
Beaumont Homestead
6.0% ABV 22.3 IBU Hop Varieties: 2 Grain Varieties: 5

Style: Farmhouse Ale

Description: Named after Henri de Valcourt—better known as the Comte de Beaumont, the Frenchman who enlisted in the American Revolution and went on to become one of Samuel Pritchard's closest allies. The beer is a celebration of the two countries and blends characteristics of a traditional French Saison with the sweetness of an American fall harvest. American corn and wild honey compliment the malted grains and French Saison yeast to give it a slightly sweet flavor. Peach and passion fruit aroma dominate the nose of this complex beer. Sniff then sip… or gulp. The fruit aroma comes from the dry hopping process.

Label Content:
• Include all government-mandated content, below
Brand name Quarrystone Brewing Co.
Class and type designation Farmhouse Ale
(type of malt beverage, eg, Ale, Lager, Stout, etc)
Name and address BREWED AND BOTTLED BY QUARRYSTONE BREWING CO.
487-B Elm Avenue
Farmingdale, NY 11902
Net contents 22 fl oz
• All of the above content must be legible, at least 2mm/6 pt font, contrast well with label background, and be placed on front of label*

Alcohol content ___% ALC/VOL
(alcohol content must be expressed to the nearest 0.1%)
• The above content must be legible, at least 2mm/6 pt font, of the same kind and size of lettering, of equally conspicuous coloring, and can be placed on front, back or side of label*

Government warning GOVERNMENT WARNING:
(1) According to the Surgeon
General, women should not drink alcoholic beverages during
pregnancy because of the risk of birth defects. (2) Consumption of
alcoholic beverages impairs your ability to drive a car or operate
machinery, and may cause health problems.
• The above content must be legible, at least 2mm/6 pt font, 25 characters at most, contrast well with label background, and can be placed on front, back or side of label*

For more information: http://www.brewrules-example.gov/beer/lbl.shtml

*INTERNAL NOTE: Size/style requirements change for 22oz labels.

Design:
• Use Middle of Label for Name, or design

For more information: http://rockmap-example.org/symbols/stdsec/rocksym-sec37.pdf

PRODUCTION
Specs:
• Main label (3.75 in x 4.25 in)
For more information: http://www.capmark-example.com/shop-bottle-type or
https://orders.capmark-example.com/capmark/start_with.cgi?tag=live-uploadyourown-cap-full#_ga=1.000000000.000000000.0000000000

Format:
• Working files: .ai, .psd, .indd
• Print-ready file: hi-res .pdf
• Other font, vector, or image files

website:
www.quarrystonebrewing-example.com

Target Market(s)

Craft Beer Drinkers

Font styles to use
Other font styles liked:
• Road Movie, Lavanderia, Nexta Rust

Requirements
Must have
• Use of Quarrystone Logo(s). Though design should incorporate the style and name of beer, the label layout should be able to be used on additional beer styles.

```html
<!DOCTYPE html>
<html lang="en">
<head>
<meta charset="utf-8">
<title>Quarrystone Brewing Co. – Beaumont Homestead Ale</title>
<link rel="stylesheet" href="https://fonts.googleapis.com/css2?family=Alfa+Slab+One&family=Arimo:wght@400;700&family=Lobster&display=swap">
<style>
  :root {
    --ink: #1a1a1a;
    --navy: #23233a;
    --orange: #ef6a22;
    --peach: #f6b085;
    --peach-light: #fbd9c3;
    --cream: #f4f1ec;
    --paper: #ffffff;
  }
  * { margin: 0; padding: 0; box-sizing: border-box; }
  html, body { width: 1059px; height: 1200px; overflow: hidden; background: var(--paper); }
  .label {
    position: relative;
    width: 1059px;
    height: 1200px;
    background: var(--paper);
    color: var(--ink);
    font-family: "Arimo", Arial, sans-serif;
  }

  /* Producer statement, rotated down the left edge */
  .producer {
    position: absolute;
    left: 84px;
    top: 22px;
    width: 940px;
    transform-origin: top left;
    transform: rotate(90deg);
    font-size: 25px;
    line-height: 32px;
    letter-spacing: 0.9px;
    white-space: nowrap;
  }

  /* Illustration areas */
  .art-honeycomb {
    position: absolute;
    left: 140px;
    top: 500px;
    width: 470px;
    height: 260px;
  }
  .art-corn {
    position: absolute;
    left: 540px;
    top: 190px;
    width: 400px;
    height: 930px;
  }

  /* Brand mark */
  .brand-mark {
    position: absolute;
    left: 193px;
    top: 55px;
    width: 460px;
    height: 460px;
  }
  .brand-mark svg { position: absolute; inset: 0; }
  .brand-mark__name {
    position: absolute;
    inset: 0;
    display: flex;
    align-items: center;
    justify-content: center;
    text-align: center;
    font-family: "Alfa Slab One", Georgia, serif;
    font-size: 50px;
    line-height: 1.15;
    color: var(--navy);
  }

  /* Product name */
  .beer-name {
    position: absolute;
    left: 180px;
    top: 760px;
    width: 620px;
    text-align: center;
    font-family: "Lobster", cursive;
    font-weight: 400;
    font-size: 150px;
    line-height: 1.1;
    color: var(--paper);
    -webkit-text-stroke: 5px var(--ink);
    paint-order: stroke fill;
    transform: rotate(-4deg);
  }
  .beer-style {
    position: absolute;
    left: 200px;
    width: 610px;
    text-align: center;
    font-family: "Alfa Slab One", Georgia, serif;
    color: var(--ink);
    text-shadow: 4px 4px 0 var(--paper), 6px 6px 0 var(--ink);
    white-space: nowrap;
  }
  .beer-style--class { top: 935px; font-size: 76px; letter-spacing: 1px; }
  .beer-style--type  { top: 1015px; font-size: 150px; letter-spacing: 48px; padding-left: 48px; line-height: 1.05; }

  /* Bottom facts line */
  .facts {
    position: absolute;
    left: 20px;
    right: 4px;
    top: 1168px;
    display: flex;
    justify-content: space-between;
    font-size: 24px;
    line-height: 1;
    white-space: nowrap;
  }

  /* Government warning, rotated up the right edge */
  .warning {
    position: absolute;
    left: 946px;
    top: 1120px;
    width: 1095px;
    transform-origin: top left;
    transform: rotate(-90deg);
    font-size: 22px;
    line-height: 27px;
  }
  .warning strong { font-weight: 700; }
</style>
</head>
<body>
<main class="label">

  <div class="producer">
    <p>BREWED AND BOTTLED BY QUARRYSTONE BREWING CO.</p>
    <p>487-B Elm Avenue Farmingdale, NY 11902</p>
  </div>

  <svg class="art-honeycomb" viewBox="0 0 470 260" role="img" aria-label="Peach honeycomb pattern with an orange and black honey bee">
    <defs>
      <radialGradient id="honeyGlow" cx="55%" cy="50%" r="60%">
        <stop offset="0" stop-color="#f6b085"/>
        <stop offset="0.6" stop-color="#fbd9c3"/>
        <stop offset="1" stop-color="#ffffff" stop-opacity="0"/>
      </radialGradient>
    </defs>
    <ellipse cx="240" cy="130" rx="235" ry="128" fill="url(#honeyGlow)"/>
  </svg>

  <svg class="art-corn" viewBox="0 0 400 930" role="img" aria-label="Illustrated ear of corn with orange and peach husks">
    <defs>
      <linearGradient id="cornTone" x1="0" y1="0" x2="1" y2="0.15">
        <stop offset="0" stop-color="#ef6a22"/>
        <stop offset="0.3" stop-color="#f6b085"/>
        <stop offset="0.6" stop-color="#f4f1ec"/>
        <stop offset="1" stop-color="#f6b085"/>
      </linearGradient>
    </defs>
    <path d="M230 10 C320 40 360 160 350 330 C340 520 300 700 250 840 C220 910 120 925 60 900 C20 880 10 820 30 700 C60 500 110 250 160 90 C180 30 200 5 230 10 Z" fill="url(#cornTone)"/>
  </svg>

  <div class="brand-mark">
    <svg width="460" height="460" viewBox="0 0 460 460" aria-hidden="true">
      <circle cx="230" cy="230" r="220" fill="#ffffff" stroke="var(--navy)" stroke-width="16"/>
    </svg>
    <p class="brand-mark__name">Quarrystone<br>Brewing Co.</p>
  </div>

  <h1 class="beer-name">Beaumont</h1>
  <p class="beer-style beer-style--class">FARMHOUSE</p>
  <p class="beer-style beer-style--type">ALE</p>

  <div class="facts">
    <span>Alcohol content 6.0% ALC/VOL 22.3 IBU</span>
    <span>Net contents 22 fl oz</span>
  </div>

  <p class="warning"><strong>GOVERNMENT WARNING:</strong> (1) According to the Surgeon General, women should not drink alcoholic beverages during pregnancy because of the risk of birth defects. (2) Consumption of alcoholic beverages impairs your ability to drive a car or operate machinery, and may cause health problems.</p>

</main>
</body>
</html>
```